Startup fashion company needs high-end, stylish and hip business cards!

We need a business card design that uses a logo that we just completed with a SketchHive artist.

Our company is Velmora. We work with fashion designers to display their designs on our website and handle all back-end fulfillment for them (fabric sourcing, garment manufacturing, customer service, etc.). The word Velmora is a play on fashion trunk shows, where designers will show their wares in a small, intimate setting. The final design should communicate high-end / luxe, chic, stylish, fashion-forward, hip!

We are using greys as our logo color (#2d2d2d, #ababab). We are also interested, for branding purposes and on our website, to use purple as a highlight color (#4a3455). I have the logo in other formats if needed.

Target Market(s)

Investors, customers, fashion designers, suppliers

Industry/Entity Type

Fashion

Contact Information for Business Card

There should be space for:
Name
Title
Address 1
Address 2
City, State Zip
USA
Phone
Email
Skype
Twitter

If it makes sense to put one or more of the contact info on the same line, that is fine if it won't be confusing.

Font styles to use
Sans Serif
Other font styles liked:
• Would like the font to be complementary to our logo font/look and feel. The logo font is Caviar Dreams with a stylized 'N' according to the logo designer.

Colors
876aae
e4daea
f3f1f8
ffffff

Requirements
Must have
• The cards will most likely printed through PrintNova and therefore must meet their upload file guidelines. There are also software templates for business cards that can be utilized. Information below from PrintNova site.
• We support a variety of file formats for uploaded designs.
• Adobe Acrobat 9 Document (*.pdf) (recommended)
• Adobe Illustrator CS3 Artwork (*.ai) (recommended)
• Adobe Photoshop CS3 Image (*.psd) (recommended)
• Bitmap Image (*.bmp)
• GIF Image (*.gif)
• JPEG Image (*.jpg,*.jpeg)
• Microsoft PowerPoint 2010 Document (*.ppt)
• Microsoft Publisher 2010 Document (*.pub)
• Microsoft Word 2010 Document (*.doc)
• PCX Image (*.pcx)
• PICT Image (*.pic,*.pict,*.pct)
• PNG Image (*.png)
• PostScript Document (*.ps)
• TIFF Image (*.tif,*.tiff)
• Windows Enhanced Metafile (*.emf)
• Windows Metafile (*.wmf)
• The templates on their site:
• Using a downloadable template for your application will ensure that your dimensions, resolution and color settings match ours.
• If you are creating a PDF document in Acrobat Distiller, please use our Distiller settings.
• Sizing:
• Full Bleed Size
• 3.62" x 2.12"
• 92 x 54 mm
• 1085 x 635 pixels
• Document Trim Size
• 3.50" x 2.00"
• 89 x 51 mm
• 1050 x 600 pixels
Nice to have
• The back can use either the full logo or just the elephant or a combination? I'm imagining a full color backside...open to other suggestions!

```html
<!DOCTYPE html>
<html lang="en">
<head>
<meta charset="utf-8">
<title>Velmora Business Card</title>
<link rel="stylesheet" href="https://fonts.googleapis.com/css2?family=Questrial&display=swap">
<style>
  :root {
    --backdrop: #e6e6e8;
    --card-white: #ffffff;
    --ink: #1e1f22;
    --charcoal: #25272a;
    --brand-purple: #3a2b73;
    --contact-text: #f1f1f3;
    --card-shadow: rgba(0, 0, 0, 0.18);
  }
  * { margin: 0; padding: 0; box-sizing: border-box; }
  html, body {
    width: 1200px;
    height: 900px;
    overflow: hidden;
    background: var(--backdrop);
    font-family: "Questrial", sans-serif;
  }
  .sheet {
    width: 1200px;
    height: 900px;
    display: flex;
    flex-direction: column;
    align-items: center;
    justify-content: center;
    gap: 60px;
  }
  .card {
    position: relative;
    width: 630px;
    height: 360px;
    background: var(--card-white);
    box-shadow: 0 6px 22px var(--card-shadow);
    overflow: hidden;
  }
  .wordmark {
    display: flex;
    align-items: center;
    gap: 12px;
    color: var(--ink);
    font-size: 46px;
    letter-spacing: 4px;
    line-height: 1;
    white-space: nowrap;
  }
  .wordmark-dot {
    width: 36px;
    height: 36px;
    border-radius: 50%;
    background: var(--brand-purple);
    flex: none;
  }
  .card-back .wordmark {
    position: absolute;
    left: 50%;
    top: 50%;
    transform: translate(-50%, -50%);
  }
  .card-front .wordmark {
    position: absolute;
    left: 30px;
    top: 82px;
  }
  .swoosh {
    position: absolute;
    inset: 0;
    width: 630px;
    height: 360px;
  }
  .swoosh-purple { fill: var(--brand-purple); }
  .swoosh-dark { fill: var(--charcoal); }
  .identity {
    position: absolute;
    left: 30px;
    bottom: 34px;
    white-space: nowrap;
  }
  .identity-name {
    color: var(--brand-purple);
    font-size: 17px;
    letter-spacing: 1.5px;
  }
  .identity-title {
    color: var(--ink);
    font-size: 13px;
    margin-top: 4px;
  }
  .contact {
    position: absolute;
    right: 22px;
    top: 26px;
    list-style: none;
    color: var(--contact-text);
    font-size: 11px;
    text-align: right;
    white-space: nowrap;
  }
  .contact-address { line-height: 1.45; margin-bottom: 14px; }
  .contact-line {
    display: flex;
    align-items: center;
    justify-content: flex-end;
    gap: 7px;
    margin-bottom: 9px;
  }
  .contact-icon {
    width: 11px;
    height: 11px;
    fill: none;
    stroke: var(--contact-text);
    stroke-width: 1.4;
    flex: none;
  }
</style>
</head>
<body>
  <main class="sheet">
    <section class="card card-back" aria-label="Card back">
      <div class="wordmark"><span class="wordmark-dot"></span>VELMORA</div>
    </section>

    <section class="card card-front" aria-label="Card front">
      <svg class="swoosh" viewBox="0 0 630 360" aria-hidden="true">
        <path class="swoosh-purple" d="M400 0 C390 150 330 280 245 360 L270 360 C380 290 436 160 448 0 Z"/>
        <path class="swoosh-dark" d="M456 0 C444 165 388 295 280 360 L630 360 L630 0 Z"/>
      </svg>

      <div class="wordmark"><span class="wordmark-dot"></span>VELMORA</div>

      <div class="identity">
        <p class="identity-name">DANIEL WHITMORE</p>
        <p class="identity-title">Managing Director</p>
      </div>

      <ul class="contact">
        <li class="contact-address">27 Orchard Lane, Suite 4<br>Brookfield, NY 10012</li>
        <li class="contact-line">555 204 7781
          <svg class="contact-icon" viewBox="0 0 12 12"><path d="M2 1.5 L4.5 1.5 L5.5 4 L4 5 Q5 7.5 7 8 L8 6.5 L10.5 7.5 L10.5 10 Q5 10.5 2 5 Z"/></svg>
        </li>
        <li class="contact-line">555 204 7782
          <svg class="contact-icon" viewBox="0 0 12 12"><rect x="3" y="1" width="6" height="10" rx="1"/><line x1="5" y1="9" x2="7" y2="9"/></svg>
        </li>
        <li class="contact-line">555 204 7783
          <svg class="contact-icon" viewBox="0 0 12 12"><rect x="1.5" y="5" width="9" height="5" rx="1"/><rect x="3.5" y="1.5" width="5" height="3.5"/></svg>
        </li>
        <li class="contact-line">hello@velmora.co
          <svg class="contact-icon" viewBox="0 0 12 12"><rect x="1" y="2.5" width="10" height="7"/><path d="M1 2.5 L6 7 L11 2.5"/></svg>
        </li>
        <li class="contact-line">www.velmora.co
          <svg class="contact-icon" viewBox="0 0 12 12"><circle cx="6" cy="6" r="5"/><ellipse cx="6" cy="6" rx="2.2" ry="5"/><line x1="1" y1="6" x2="11" y2="6"/></svg>
        </li>
      </ul>
    </section>
  </main>
</body>
</html>
```